Tito - Lumora Estudos

2x Design Concepts for the home page and interior pages based on the attached brief and powerpoint presentation.

Colours: see 2.1 logo and heading for logo colours and website colours

Home Page: (please see attached file)
1)Logo to appear in the top left, heading to include telephone numbers and a best price (credibility stamp) - see 2.1
2)the toolbar is to be centered at the top. Emphasis must be placed on the 5 easy steps to study english in Australia - see 2.2
3) modules. 5x modules required in the home page for: home page image rotator, online quote tool, enquiry form, best deals, quick links (there are 2 examples for the quick links module - open to suggestions) - see 2.3
4) footer. the footer is to include partner logos with hyperlinks to the partner websites. with a copywright section at the base - see 2.4
5) 2.5 is the basic idea - open to design suggestions. The website objective is to submit an online quote or contact Lumora Estudos.

Internal Page: - see 3-
open to all suggestion. Require a lot of space for internal custom design concepts (these are taking place inhouse). The interior page must have a side module toolbar to include:
1) a modified online quote tool
2) modified enquiry form
3) modified quick links section

Target Market(s)

target market is young (17-30yrs) Brazilians looking to study English in Australia or continue studying English in Australia that can also acquire visa sponsorship.

The buyer will be the parents of the students. the design must appeal to both markets.

Number of Pages Required

2 pages

Requirements
Must have
• see project overview
2x design concepts for the home page and interior page
professional, clean, simple and easy to navigate

```html
<!DOCTYPE html>
<html lang="pt">
<head>
<meta charset="utf-8">
<title>Lumora Estudos</title>
<link href="https://fonts.googleapis.com/css2?family=Arimo:ital,wght@0,400;0,700;1,400&display=swap" rel="stylesheet">
<style>
:root{
  --green:#0d5a3a;
  --green-btn:#10915a;
  --navy:#1f4678;
  --orange:#e4761c;
  --orange-light:#f7a21a;
  --text:#222;
  --muted:#444;
  --row:#fdeecb;
  --panel:#e8efec;
  --line:#c9c9c9;
}
*{box-sizing:border-box;margin:0;padding:0}
html,body{width:1115px;height:1200px;overflow:hidden}
body{position:relative;background:#fff;font-family:"Arimo",Arial,sans-serif;color:var(--text)}
.abs{position:absolute}

/* header */
.nav-band{left:0;top:0;width:1115px;height:60px}
.nav{left:373px;top:8px;display:flex;gap:0;font-size:16px}
.nav a{color:#222;text-decoration:none;padding:7px 19px;border-radius:6px}
.nav a.active{background:var(--navy);color:#fff;box-shadow:inset 0 -2px 0 rgba(0,0,0,.2)}
.badge{left:846px;top:-6px;width:154px;height:100px}
.logo{left:118px;top:62px;color:var(--green);font-weight:700;font-size:17px;letter-spacing:.3px;display:flex;align-items:center;gap:6px}
.logo .dot{width:12px;height:12px;border-radius:50%;background:var(--orange)}
.logo small{display:block;font-size:10px;color:var(--navy);text-align:right;margin-top:-2px}
.phone{top:78px;display:flex;align-items:center;gap:10px;font-weight:700;font-size:19px;color:#222}
.flag{width:35px;height:24px;border:1px solid #bbb}
.steps{left:119px;top:132px;display:flex;gap:24px;align-items:baseline;font-weight:700;color:#555;font-size:16px}
.steps .lead{color:var(--green);font-size:19px;margin-right:2px}
.steps b{color:var(--green);font-size:19px;margin-right:3px}

/* hero */
.hero{left:122px;top:209px;width:528px;height:287px;background:#fff;box-shadow:0 0 5px rgba(0,0,0,.2);padding:5px}
.hero .ph{width:100%;height:100%;background:linear-gradient(120deg,#e9e4df,#b88e70 40%,#8aa3c0 75%,#e6e6e6)}

/* study cards */
.card{left:119px;width:533px;height:169px;border:3px solid;border-radius:3px;background:#fff}
.card .ph{position:absolute;left:20px;top:21px;width:190px;height:126px;border:3px solid}
.card h3{position:absolute;left:222px;top:22px;font-size:14.5px}
.card p{position:absolute;left:222px;top:52px;width:292px;font-size:11px;line-height:13.6px;color:#333}
.card .more{position:absolute;right:15px;bottom:20px;font-size:11px;font-weight:700;text-decoration:none}
.c-orange{border-color:#f6d9a7;border-bottom-color:var(--orange);border-image:linear-gradient(#fbe3b4,var(--orange)) 1}
.c-orange .ph{border-color:#f8e6c5;background:linear-gradient(135deg,#c9c4b5,#6f8d56 60%,#dcd6c8)}
.c-orange h3,.c-orange .more{color:var(--orange)}
.c-navy{border-image:linear-gradient(#aecbee,var(--navy)) 1}
.c-navy .ph{border-color:#a9c7ef;background:linear-gradient(180deg,#8fc0e8,#4d7fb0 55%,#3c3533)}
.c-navy h3,.c-navy .more{color:var(--navy)}
.c-green{border-image:linear-gradient(#a8dcc0,var(--green)) 1}
.c-green .ph{border-color:#a9dbbf;background:linear-gradient(135deg,#caa66d,#e9e0cc 50%,#586b7c)}
.c-green h3,.c-green .more{color:var(--green)}

/* quote tool */
.quote{left:676px;top:205px;width:328px}
.quote h2{color:var(--navy);font-size:25px;font-weight:700;letter-spacing:.2px;text-shadow:0 1px 0 #aab}
.label{font-weight:700;font-size:15px;color:#222}
.radios{display:grid;grid-template-columns:113px 114px 100px;row-gap:12px;margin-top:13px;font-size:13px}
.radios span{display:flex;align-items:center;gap:6px}
.radio{width:14px;height:14px;border-radius:50%;background:radial-gradient(#333 0 2.5px,#fff 3px);border:1px solid #bbb;box-shadow:0 1px 1px rgba(0,0,0,.15)}
.select{left:793px;top:375px;width:155px;height:25px;border:1px solid #ccc;font-size:12px;padding:6px 8px;background:#fff}
.select .arr{position:absolute;right:0;top:0;width:27px;height:23px;background:#d6d6d6;display:flex;align-items:center;justify-content:center}
.btn-orange{left:679px;top:420px;width:135px;height:33px;border-radius:17px;background:linear-gradient(#f9b23c,#e66e12);color:#fff;font-weight:700;font-size:15px;display:flex;align-items:center;justify-content:center;box-shadow:0 1px 2px rgba(0,0,0,.3)}
.pay{left:679px;top:470px;display:flex;gap:8px}
.pay i{width:42px;height:22px;border:1px solid #ccc;background:linear-gradient(#fafafa,#e3e3e3)}

/* deals */
.deals{left:676px;top:521px;width:328px}
.deals h2{font-size:18px;font-weight:700;margin-left:15px;margin-bottom:15px}
.deals .row{display:flex;justify-content:space-between;height:31px;align-items:center;padding:0 14px 0 15px;font-size:14px}
.deals .row:nth-child(odd){background:var(--row)}
.deals .row span:first-child{color:var(--orange)}
.deals .link{display:inline-block;margin:6px 0 0 17px;font-style:italic;font-size:14px;color:#333;border-bottom:1px solid #555}

/* contact */
.contact{left:676px;top:764px;width:328px;height:325px;border:1px solid #ddd;box-shadow:0 0 3px rgba(0,0,0,.1);padding:7px}
.contact .inner{background:var(--panel);height:100%;padding:13px 16px}
.contact h2{text-align:center;color:var(--green);font-size:25px;font-weight:700;margin-bottom:15px}
.field{background:#fff;border:1px solid #bbb;height:31px;margin-bottom:8px;padding:7px 9px;font-size:14px}
.field.msg{height:83px}
.send{display:block;margin:11px auto 0;width:105px;height:31px;border-radius:15px;background:linear-gradient(#2bb879,#0b6b42);color:#fff;font-weight:700;font-size:17px;text-align:center;line-height:31px}

/* footer */
.footer{left:0;top:1096px;width:1115px;height:104px;background:linear-gradient(#fff,#e4e4e4)}
.copy{right:113px;top:1148px;text-align:right;font-size:11.5px;line-height:14px;color:#333}
</style>
</head>
<body>

<svg class="abs nav-band" viewBox="0 0 1115 60" aria-hidden="true">
  <defs><linearGradient id="band" x1="0" y1="0" x2="0" y2="1"><stop offset="0" stop-color="#ffffff"/><stop offset="1" stop-color="#dcdcdc"/></linearGradient></defs>
  <path d="M0 8 H270 C295 8 300 48 335 48 H790 C825 48 830 8 855 8 H1115 V0 H0 Z" fill="#f0f0f0"/>
  <path d="M270 8 C295 8 300 48 335 48 H790 C825 48 830 8 855 8 Z" fill="url(#band)" stroke="#cfcfcf"/>
</svg>
<nav class="abs nav">
  <a class="active" href="#">Home</a><a href="#">Promocoes</a><a href="#">Contato</a><a href="#">Blog</a>
</nav>

<svg class="abs badge" viewBox="0 0 154 100" role="img" aria-label="Best price stamp">
  <defs><linearGradient id="burst" x1="0" y1="0" x2="0" y2="1"><stop offset="0" stop-color="#ffb52e"/><stop offset="1" stop-color="#f08a12"/></linearGradient></defs>
  <polygon fill="url(#burst)" points="77,100 67,88 52,92 48,78 33,76 36,62 22,54 32,43 24,30 38,26 36,10 52,12 58,0 96,0 102,12 118,10 116,26 130,30 122,43 132,54 118,62 121,76 106,78 102,92 87,88"/>
  <text x="77" y="27" text-anchor="middle" fill="#fff" font-family="Arimo, Arial, sans-serif" font-weight="700" font-size="24">BEST</text>
  <text x="77" y="55" text-anchor="middle" fill="#fff" font-family="Arimo, Arial, sans-serif" font-weight="700" font-size="24">PRICE</text>
</svg>

<div class="abs logo"><span class="dot"></span><div>LUMORA ESTUDOS<small>.com.br</small></div></div>

<div class="abs phone" style="left:327px"><span class="flag" style="background:#1d2f7a"></span>0 800 555 014</div>
<div class="abs phone" style="left:516px"><span class="flag" style="background:#1f9a3c"></span>1 800 555 014</div>

<div class="abs steps">
  <span class="lead">5 STEPS EXPERT IN ENGLISH</span>
  <span><b>1</b>Cidades</span><span><b>2</b>Escolas</span><span><b>3</b>Passagem Aerea</span><span><b>4</b>Visto</span><span><b>5</b>Dehalhes Finais</span>
</div>

<div class="abs hero"><div class="ph" role="img" aria-label="Group of smiling young students holding notebooks"></div></div>

<article class="abs card c-orange" style="top:523px">
  <div class="ph" role="img" aria-label="Smiling student leaning on a stack of books"></div>
  <h3>Study Abroad</h3>
  <p>Lorem ipsum dolor sit amet, consectetur adipisicing elit, sed do eiusmod tempor incididunt ut labore et dolore magna aliqua. Ut enim ad minim veniam, quis nostrud exercitation ullamco laboris nisi ut aliquip ex ea commodo consequat.</p>
  <a class="more" href="#">more &gt;&gt;</a>
</article>
<article class="abs card c-navy" style="top:723px">
  <div class="ph" role="img" aria-label="Group of friends under a blue sky"></div>
  <h3>Study Abroad</h3>
  <p>Lorem ipsum dolor sit amet, consectetur adipisicing elit, sed do eiusmod tempor incididunt ut labore et dolore magna aliqua. Ut enim ad minim veniam, quis nostrud exercitation ullamco laboris nisi ut aliquip ex ea commodo consequat.</p>
  <a class="more" href="#">more &gt;&gt;</a>
</article>
<article class="abs card c-green" style="top:922px">
  <div class="ph" role="img" aria-label="Students studying together in a library"></div>
  <h3>Study Abroad</h3>
  <p>Lorem ipsum dolor sit amet, consectetur adipisicing elit, sed do eiusmod tempor incididunt ut labore et dolore magna aliqua. Ut enim ad minim veniam, quis nostrud exercitation ullamco laboris nisi ut aliquip ex ea commodo consequat.</p>
  <a class="more" href="#">more &gt;&gt;</a>
</article>

<section class="abs quote">
  <h2>CONTACAO ON LINE</h2>
  <div class="label" style="margin-top:20px">CIDADE</div>
  <div class="radios">
    <span><i class="radio"></i>Sydney</span><span><i class="radio"></i>Melbourne</span><span><i class="radio"></i>Gold Coast</span>
    <span><i class="radio"></i>Brisbane</span><span><i class="radio"></i>Perth</span><span><i class="radio"></i>Adelaide</span>
    <span><i class="radio"></i>Byron Bay</span>
  </div>
  <div class="label" style="margin-top:22px">DURACAO</div>
</section>
<div class="abs select">2 Semanas
  <span class="arr"><svg width="12" height="8" viewBox="0 0 12 8"><path d="M0 0H12L6 8Z" fill="#888"/></svg></span>
</div>
<div class="abs btn-orange">PROCURAR</div>
<div class="abs pay" aria-label="Accepted payment methods"><i></i><i></i><i></i><i></i></div>

<section class="abs deals">
  <h2>IN AUSTRALIA</h2>
  <div>
    <div class="row" style="background:none"><span>Brisbane</span><span>from $89*</span></div>
    <div class="row" style="background:var(--row)"><span>Balina Byron Bay</span><span>from $79*</span></div>
    <div class="row" style="background:none"><span>Gold Coast</span><span>from $75*</span></div>
    <div class="row" style="background:var(--row)"><span>Hamilton Island</span><span>from $159*</span></div>
    <div class="row" style="background:none"><span>Launceston</span><span>from $89*</span></div>
  </div>
  <a class="link">more domestic flights</a>
</section>

<section class="abs contact">
  <div class="inner">
    <h2>ENTRE EM CONTATO</h2>
    <div class="field">Name</div>
    <div class="field">E-mail</div>
    <div class="field">Telephone</div>
    <div class="field msg">Message</div>
    <span class="send">SEND</span>
  </div>
</section>

<footer class="abs footer"></footer>
<div class="abs copy">Copyright (c) www.lumoraestudos.com 2009<br>All rights reserved</div>

</body>
</html>
```